Criação de Cartao de Visita para Consultoria de Negócios
A empresa queria:
" CONSULTORIA PARA EMPRESAS E GRUPOS FAMILIARES PARA REESTRUTURAÇÃO FINANCEIRA E DE NEGÓCIOS "

```html
<!DOCTYPE html>
<html lang="pt-BR">
<head>
<meta charset="utf-8">
<title>Norvale consulting – Cartão de Visita</title>
<link rel="stylesheet" href="https://fonts.googleapis.com/css2?family=Open+Sans:wght@400;600;700&display=swap">
<style>
  :root {
    --stage: #e8e6e2;
    --teal-dark: #1c4f52;
    --teal: #2a6667;
    --teal-light: #3a7a79;
    --paper: #ffffff;
    --paper-shade: #eef0f0;
    --ink: #2a6667;
    --muted: #8a9393;
    --rule: #c9d1d1;
  }
  * { box-sizing: border-box; margin: 0; padding: 0; }
  html, body { width: 1200px; height: 1200px; overflow: hidden; }
  body {
    background: var(--stage);
    font-family: "Open Sans", sans-serif;
    display: flex;
    flex-direction: column;
    align-items: center;
    justify-content: center;
    gap: 60px;
  }
  .card {
    width: 900px;
    height: 514px;
    border-radius: 6px;
    box-shadow: 0 14px 34px rgba(0,0,0,0.18);
    position: relative;
    overflow: hidden;
  }
  /* Front */
  .card--front {
    background: linear-gradient(135deg, var(--teal-light) 0%, var(--teal) 45%, var(--teal-dark) 100%);
    display: flex;
    align-items: center;
    justify-content: center;
  }
  .brand {
    display: flex;
    align-items: center;
    gap: 16px;
    font-family: "Open Sans", sans-serif;
    font-weight: 400;
  }
  .brand__dot {
    width: 26px; height: 26px; border-radius: 50%;
  }
  .brand__name { letter-spacing: 1px; }
  .card--front .brand { color: #ffffff; font-size: 54px; }
  .card--front .brand__dot { background: #ffffff; }

  /* Back */
  .card--back {
    background: linear-gradient(160deg, var(--paper) 0%, var(--paper) 55%, var(--paper-shade) 100%);
    display: flex;
    align-items: center;
    padding: 0 70px;
  }
  .card--back .brand { color: var(--ink); font-size: 34px; width: 360px; }
  .card--back .brand__dot { background: var(--ink); width: 18px; height: 18px; }
  .divider {
    width: 2px; height: 250px; background: var(--rule); margin: 0 50px 0 10px;
  }
  .contact { color: var(--ink); }
  .contact__name { font-size: 32px; font-weight: 700; line-height: 1.1; }
  .contact__role { font-size: 17px; color: var(--muted); margin-bottom: 26px; }
  .contact__list { list-style: none; display: flex; flex-direction: column; gap: 12px; }
  .contact__item { display: flex; align-items: center; gap: 12px; font-size: 17px; font-weight: 600; }
  .icon {
    width: 26px; height: 26px; border-radius: 50%; background: var(--ink);
    display: flex; align-items: center; justify-content: center; flex-shrink: 0;
  }
  .icon svg { width: 14px; height: 14px; }
</style>
</head>
<body>
  <section class="card card--front" aria-label="Frente do cartão">
    <div class="brand">
      <span class="brand__dot"></span>
      <span class="brand__name">Norvale consulting</span>
    </div>
  </section>

  <section class="card card--back" aria-label="Verso do cartão">
    <div class="brand">
      <span class="brand__dot"></span>
      <span class="brand__name">Norvale consulting</span>
    </div>
    <div class="divider"></div>
    <div class="contact">
      <p class="contact__name">Nome sobrenome</p>
      <p class="contact__role">Cargo</p>
      <ul class="contact__list">
        <li class="contact__item">
          <span class="icon"><svg viewBox="0 0 24 24" fill="#fff"><path d="M6.6 10.8a15.1 15.1 0 0 0 6.6 6.6l2.2-2.2c.3-.3.7-.4 1-.2 1.1.4 2.3.6 3.6.6.6 0 1 .4 1 1V20c0 .6-.4 1-1 1A17 17 0 0 1 3 4c0-.6.4-1 1-1h3.5c.6 0 1 .4 1 1 0 1.3.2 2.5.6 3.6.1.3 0 .7-.2 1z"/></svg></span>
          +55 00 00000-0000
        </li>
        <li class="contact__item">
          <span class="icon"><svg viewBox="0 0 24 24" fill="none" stroke="#fff" stroke-width="2"><rect x="3" y="5" width="18" height="14" rx="1"/><path d="M3 6l9 7 9-7"/></svg></span>
          email@norvaleconsulting.com.br
        </li>
        <li class="contact__item">
          <span class="icon"><svg viewBox="0 0 24 24" fill="none" stroke="#fff" stroke-width="2"><circle cx="12" cy="12" r="9"/><path d="M3 12h18M12 3c3 3.5 3 14.5 0 18M12 3c-3 3.5-3 14.5 0 18"/></svg></span>
          www.norvaleconsulting.com.br
        </li>
      </ul>
    </div>
  </section>
</body>
</html>
```